Consulting, Investors, Joint Venture Website

Founded in April 2018, Marendo Consultants Limited (MCL) is an advisory consulting firm specializing in engaging investors in business ventures in Tanzania.
With extensive experience in construction, energy, oil and gas and the legal professions, our team assembles our expertise that allows foreign investors to set foot and flourish in the Tanzanian market.
MCL is locally owned, founded and registered. Our shareholders are cultured Tanzanian citizens with extensive corporate experience in South Africa, Tanzania, United Kingdom and the United States.

Our mission is to provide responsive and unrivalled professional advice from learned and experienced professionals versed in the local market, with an understanding of the cultural and logistical challenges faced by foreign investors.

Our vision is to provide a complete investor’s package that initiates with company registration, compliance and documentation services and ultimately operational facilitation services.

Target Market(s)

Foreign Investors, International companies

Industry/Entity Type

Business Consultant

Number of Pages Required

5+ page

Requirements
Must have
• It will be 5 pages - Home, About Us, Services, Portfolio, Contact Us
Nice to have
• if it can look like https://www.plorvex.example/
• or https://www.dunetri.example or http://www.quillbrook.example/

```html
<!DOCTYPE html>
<html lang="en">
<head>
<meta charset="utf-8">
<title>Marendo Consultants Limited</title>
<link rel="stylesheet" href="https://fonts.googleapis.com/css2?family=Quicksand:wght@600;700&family=Jost:wght@400;500;600&family=Lato:wght@400;700&display=swap">
<style>
:root{
  --orange:#f7941d;
  --orange-soft:#f9c98d;
  --blue:#0d4f9e;
  --blue-band:#2c65ab;
  --ink:#222;
  --body:#555;
  --white:#fff;
  --grey-btn:#c9c9c9;
}
*{box-sizing:border-box;margin:0;padding:0}
html,body{width:1200px;height:2335px;overflow:hidden;background:var(--white)}
body{font-family:"Lato",sans-serif;color:var(--body)}
.page{position:relative;width:1200px;height:2335px;overflow:hidden}
.abs{position:absolute}

/* header */
.topline{left:0;top:0;width:1200px;height:5px;background:var(--orange)}
.brand{left:78px;top:38px;display:flex;align-items:center;gap:14px}
.brand-mark{width:44px;height:44px;background:var(--orange)}
.brand-name{font-family:"Jost",sans-serif;font-weight:600;font-size:27px;letter-spacing:1.5px;color:var(--blue);line-height:1}
.brand-name small{display:block;font-size:13px;letter-spacing:5px;margin-top:4px}
.nav{left:446px;top:50px;display:flex;font-family:"Jost",sans-serif;font-size:16px;color:#444}
.nav a{color:inherit;text-decoration:none;margin-right:31px}
.nav a.active{color:var(--orange)}
.nav-pointer{left:456px;top:112px}
.search{left:904px;top:42px;width:218px;height:40px;border:2px solid var(--orange);border-radius:20px;overflow:hidden;display:flex}
.search span{flex:1;background:var(--orange);color:var(--white);font-size:13px;line-height:36px;padding-left:13px}
.search i{width:42px;background:var(--white);display:flex;align-items:center;justify-content:center}

/* hero */
.hero{left:0;top:124px;width:1200px;height:573px;background:linear-gradient(100deg,#3d4450 0%,#6b707a 35%,#8a8c92 60%,#5c5f66 100%)}
.hero-shade{left:0;top:124px;width:1200px;height:573px;background:rgba(20,25,35,.35)}
.hero-title{left:0;top:292px;width:1200px;text-align:center;font-family:"Quicksand",sans-serif;font-weight:700;font-size:40px;color:var(--orange);letter-spacing:1px;text-shadow:0 2px 3px rgba(0,0,0,.6)}
.hero-sub{left:0;top:356px;width:1200px;text-align:center;font-family:"Jost",sans-serif;font-size:31px;color:var(--white)}
.hero-text{left:0;top:404px;width:1200px;text-align:center;font-size:15px;line-height:25px;color:var(--white)}
.btn{top:487px;height:55px;border-radius:28px;font-family:"Jost",sans-serif;font-size:20px;color:var(--white);display:flex;align-items:center;justify-content:center;letter-spacing:.5px}
.btn-ghost{left:408px;width:185px;border:2px solid var(--white)}
.btn-solid{left:605px;width:187px;background:var(--orange)}
.arrow{width:52px;height:52px;border-radius:50%;display:flex;align-items:center;justify-content:center}
.arrow-prev{left:51px;top:396px;background:var(--orange)}
.arrow-next{left:1096px;top:396px;background:var(--grey-btn)}

/* portfolio */
.section-title{font-family:"Quicksand",sans-serif;font-weight:700;font-size:37px;color:var(--orange)}
.portfolio-title{left:79px;top:754px}
.portfolio-lead{left:79px;top:814px;font-family:"Jost",sans-serif;font-size:23px;line-height:30px;color:var(--orange)}
.portfolio-text{left:79px;top:893px;width:250px;font-size:14.5px;line-height:25px}
.enquiry{left:79px;top:988px;font-family:"Jost",sans-serif;font-size:17px;color:var(--orange);text-decoration:underline}
.pager{top:979px;width:42px;height:42px;border-radius:50%;display:flex;align-items:center;justify-content:center}
.pager-prev{left:253px;background:var(--blue)}
.pager-next{left:300px;background:#8fb0d9}
.card{top:761px;width:333px;height:260px;overflow:hidden}
.card-photo{position:absolute;inset:0;background:linear-gradient(135deg,#c9d3de 0%,#7d8a99 45%,#2f3a4a 100%)}
.card-caption{position:absolute;left:10px;top:177px;width:313px;height:70px;background:var(--white);padding:10px 13px}
.card-caption h3{font-family:"Jost",sans-serif;font-weight:500;font-size:22px;color:var(--blue);line-height:28px}
.card-caption p{font-size:13px;color:#777;margin-top:4px}

/* features */
.band{left:0;top:1218px;width:1200px;height:469px;background:linear-gradient(110deg,#2a5fa4,#3a73b8 50%,#2b62a8)}
.feature{top:1094px;width:344px;height:260px;text-align:center;padding-top:32px}
.feature svg{display:block;margin:0 auto}
.feature h3{font-family:"Jost",sans-serif;font-weight:500;font-size:21px;line-height:28px;color:var(--ink);margin-top:16px}
.feature p{font-size:14px;line-height:25px;color:var(--ink);margin-top:10px}
.feature-1{left:84px;background:var(--orange-soft)}
.feature-2{left:428px;background:var(--orange)}
.feature-2 p{color:var(--white)}
.feature-3{left:772px;background:var(--orange-soft)}
.trust-title{left:0;top:1402px;width:1200px;text-align:center;font-family:"Jost",sans-serif;font-size:31px;color:var(--white)}
.trust-text{left:262px;top:1465px;width:676px;text-align:center;font-size:14.5px;line-height:25px;color:var(--white)}
.play{left:568px;top:1567px}

/* about */
.about-title{left:79px;top:1745px;color:var(--blue)}
.about-title span{color:var(--orange)}
.about-photo{left:78px;top:1824px;width:249px;height:165px;background:linear-gradient(135deg,#e6eef6,#9fb6cf 55%,#5d738c)}
.about-side{left:345px;top:1818px;width:390px;font-size:14.5px;line-height:25px}
.about-full{left:79px;top:2007px;width:658px;font-size:14.5px;line-height:25px}
.sector{left:790px;width:332px;height:72px;border-radius:36px;display:flex;align-items:center;padding-left:28px;gap:20px;font-family:"Jost",sans-serif;font-size:23px;color:var(--white)}
.sector.orange{background:var(--orange)}
.sector.blue{background:var(--blue)}

/* footer */
.footer{left:0;top:2228px;width:1200px;height:107px;background:var(--blue);text-align:center;font-size:15px;line-height:107px;color:var(--white)}
.footer span{color:var(--orange)}
</style>
</head>
<body>
<div class="page">

  <div class="abs topline"></div>
  <div class="abs brand"><div class="brand-mark"></div><div class="brand-name">MARENDO<small>CONSULTANTS</small></div></div>
  <nav class="abs nav"><a class="active" href="#">Home</a><a href="#">About Us</a><a href="#">Services</a><a href="#">Portfolio</a><a href="#">Contact</a></nav>
  <svg class="abs nav-pointer" width="24" height="12"><polygon points="0,12 12,0 24,12" fill="var(--blue)"/></svg>
  <div class="abs search"><span>Search here...</span><i><svg width="20" height="20" fill="none" stroke="#0d4f9e" stroke-width="2"><circle cx="8" cy="8" r="6"/><line x1="12.5" y1="12.5" x2="18" y2="18"/></svg></i></div>

  <div class="abs hero" role="img" aria-label="Business team meeting in a bright office"></div>
  <div class="abs hero-shade"></div>
  <div class="abs hero-title">MARENDO CONSULTANTS LIMITED</div>
  <div class="abs hero-sub">Solution &amp; Consulting</div>
  <div class="abs hero-text">Lorem Ipsum is simply dummy text of the printing and typesetting industry.<br>Lorem Ipsum has been the industry's standard dummy text ever since the 1500s,</div>
  <div class="abs btn btn-ghost">OUR SERVICES</div>
  <div class="abs btn btn-solid">CONTACT US</div>
  <div class="abs arrow arrow-prev"><svg width="14" height="14" fill="none" stroke="#fff" stroke-width="2.5"><polyline points="9,2 4,7 9,12"/></svg></div>
  <div class="abs arrow arrow-next"><svg width="14" height="14" fill="none" stroke="#fff" stroke-width="2.5"><polyline points="5,2 10,7 5,12"/></svg></div>

  <h2 class="abs section-title portfolio-title">Our Portfolio</h2>
  <div class="abs portfolio-lead">Our work will take you<br>a next level.</div>
  <p class="abs portfolio-text">Lorem Ipsum is simply dummy text of<br>the printing and typesetting industry<br>standard dummy text ever&nbsp; 1500s.</p>
  <a class="abs enquiry">FOR ENQUIRY</a>
  <div class="abs pager pager-prev"><svg width="12" height="12" fill="none" stroke="#fff" stroke-width="2.5"><polyline points="8,1 3,6 8,11"/></svg></div>
  <div class="abs pager pager-next"><svg width="12" height="12" fill="none" stroke="#fff" stroke-width="2.5"><polyline points="4,1 9,6 4,11"/></svg></div>

  <div class="abs card" style="left:383px"><div class="card-photo" role="img" aria-label="Colleagues reviewing work at a laptop"></div><div class="card-caption"><h3>Startup Funding</h3><p>Finance</p></div></div>
  <div class="abs card" style="left:748px"><div class="card-photo" role="img" aria-label="Business partners shaking hands"></div><div class="card-caption"><h3>Startup Funding</h3><p>Finance</p></div></div>
  <div class="abs card" style="left:1113px"><div class="card-photo" role="img" aria-label="Business meeting"></div><div class="card-caption"><h3>Startup Funding</h3><p>Finance</p></div></div>

  <div class="abs band" role="img" aria-label="Handshake over a city skyline in blue tones"></div>
  <div class="abs feature feature-1">
    <svg width="76" height="62" fill="none" stroke="#fff" stroke-width="3"><circle cx="30" cy="30" r="24"/><polyline points="30,16 30,30 40,36"/><circle cx="58" cy="46" r="10"/><circle cx="58" cy="46" r="4"/></svg>
    <h3>On Time Services</h3><p>Lorem Ipsum is simply dummy text of<br>the printing and typesetting industry<br>standard dummy text ever&nbsp; 1500s.</p>
  </div>
  <div class="abs feature feature-2">
    <svg width="62" height="62" fill="#fff"><circle cx="14" cy="10" r="6"/><rect x="7" y="18" width="14" height="26" rx="3"/><circle cx="31" cy="8" r="7"/><rect x="23" y="17" width="16" height="32" rx="3"/><circle cx="48" cy="10" r="6"/><rect x="41" y="18" width="14" height="26" rx="3"/></svg>
    <h3>Experienced Team</h3><p>Lorem Ipsum is simply dummy text of<br>the printing and typesetting industry<br>standard dummy text ever&nbsp; 1500s.</p>
  </div>
  <div class="abs feature feature-3">
    <svg width="92" height="62" fill="none" stroke="#fff" stroke-width="3"><rect x="4" y="36" width="12" height="22"/><rect x="22" y="26" width="12" height="32"/><rect x="40" y="40" width="12" height="18"/><polyline points="4,28 20,14 34,22"/><circle cx="62" cy="20" r="14"/><line x1="72" y1="30" x2="86" y2="46"/></svg>
    <h3>Analyze your Business</h3><p>Lorem Ipsum is simply dummy text of<br>the printing and typesetting industry<br>standard dummy text ever&nbsp; 1500s.</p>
  </div>
  <div class="abs trust-title">We are trusted by more than 10,000 clients</div>
  <p class="abs trust-text">Lorem Ipsum is simply dummy text of the printing and typesetting industry. Lorem Ipsum has been the industry's standard dummy text ever since the 1500s, when unknown printer took a galley of type and scrambled it make a1500s.</p>
  <svg class="abs play" width="62" height="62"><circle cx="31" cy="31" r="29" fill="var(--orange)" stroke="#fff" stroke-width="4"/><polygon points="25,19 25,43 44,31" fill="#fff"/></svg>

  <h2 class="abs section-title about-title">About <span>Us</span></h2>
  <div class="abs about-photo" role="img" aria-label="Two colleagues working with a calculator"></div>
  <p class="abs about-side">Lorem Ipsum is simply dummy text of the printing and typesetting industry. Lorem Ipsum has been the industry's standard dummy text ever since the 1500s, when an unknown printer took a galley of type and scrambled it to make a type specimen book. It has survived not only five centuries, but also the leap into electronic typesetting, remaining essentially unchanged.</p>
  <p class="abs about-full">Lorem Ipsum is simply dummy text of the printing and typesetting industry. Lorem Ipsum has been the industry's standard dummy text ever since the 1500s, when an unknown printer took a galley of type and scrambled it to make a type specimen book. It has survived not only five centuries, but also the leap into electronic typesetting, remaining essentially unchanged.Lorem Ipsum is simply dummy text of the printing and typesetting industry. Lorem Ipsum has been the industry's standard dummy text ever since the 1500s, when an unknown printer took a galley of type and scrambled it to make a type specimen book.</p>

  <div class="abs sector orange" style="top:1824px"><svg width="44" height="40" fill="none" stroke="#fff" stroke-width="2.5"><rect x="3" y="3" width="38" height="34"/><rect x="10" y="12" width="10" height="12"/><line x1="26" y1="12" x2="34" y2="12"/><line x1="26" y1="20" x2="34" y2="20"/></svg>Construction</div>
  <div class="abs sector blue" style="top:1906px"><svg width="44" height="40" fill="none" stroke="#fff" stroke-width="2.5"><circle cx="22" cy="17" r="10"/><line x1="17" y1="30" x2="27" y2="30"/><line x1="18" y1="35" x2="26" y2="35"/><line x1="22" y1="1" x2="22" y2="4"/><line x1="5" y1="17" x2="8" y2="17"/><line x1="36" y1="17" x2="39" y2="17"/></svg>eEnergy</div>
  <div class="abs sector orange" style="top:1990px"><svg width="44" height="40" fill="none" stroke="#fff" stroke-width="2.5"><polyline points="12,38 22,3 32,38"/><line x1="16" y1="24" x2="28" y2="24"/><line x1="14" y1="32" x2="30" y2="32"/><line x1="4" y1="38" x2="40" y2="38"/></svg>Oil and gas</div>
  <div class="abs sector blue" style="top:2074px"><svg width="44" height="40" fill="none" stroke="#fff" stroke-width="2.5"><rect x="6" y="12" width="32" height="24" rx="3"/><path d="M16 12V6h12v6"/><line x1="6" y1="22" x2="38" y2="22"/></svg>The legal professions</div>

  <footer class="abs footer">© 2018&nbsp; <span>MARENDO CONSULTANT</span> . All rights reserved.</footer>
</div>
</body>
</html>
```